Etiketten für Ätherische Öle, Extrakte und Speiseöle gesucht
Zielgruppe
Wir verkaufen natürlich Produkte. Ätherische öle, Extrakte, Speise öle.
Wir verkaufen im Webshop, Kaufwelt und auch im Betrieb.
https://www.natur-sefo.com
Wir verkaufen hauptsächlich innerhalb Italiens und Deutschland daher doppel sprachig.
Aufgabenstellung
Guten Tag
Bitte verwenden Sie! : * beispiel_10_ml_etikett_nachbau.jpg *
Da mir die kleinste Größe die wichtigste ist habe ich ein beispiel Hochgeladen. Das kleinste Etikett lässt sich öffnen und daher sind nur 7 cm ersichtlich und man muss das Etikett aufmachen.
Habe ein Beispiel Hochgeladen. Aber bitte einfach kreativ sein. *Anhang: beispiel Etikett*
Sobald ich eine Art vom kelinsten habe würde ich dies für die 2 anderen Größen übernehmen aber das man Sie irgendwie gut unterscheiden kann da dies dann komplett andere Produkte (Extrakte/Speise öl) sein werden.
Erstellung von drei unterschiedlichen Größen von Etiketten mit folgenden Eigenschaften:
Am wichtigsten ist mir das kleinste Etikett da dies auch am schwersten ist daher habe ich die anderen Größen nun gelöscht!
• 10 ml Länge: 155 mm Breite: 32 mm.
Brauche 3 unterschiedliche Grund Farben: z. B. Ätherische Öle (Grün) Extrakte (Rot) Speiseöle (gelb). Die Farben lasse ich sie entscheiden.
Die Etiketten müssen 2 Sprachen (Deutsch / Italienisch) sein deshalb muss dieses berücksichtigt werden.
Anbei finden Sie:
• Logo (Bild Logo)
• Beispiel Text ätherische Öle
• Bilder der aktuellen Flaschen
Unter https://www.natur-sefo.com/de finden Sie meine Seite
Anmerkung: Im Anhang: *Back*
Habe ich mein Logo mit Firmennamen ; Bio des Hollmer Tobias
Da ich jedoch nicht alle Produkte im biologischen Anbau habe und mein Logo zu miss Verständnis führen könnte habe ich ein Bildliches Logo gemacht das ich fortan auf meinen Produkten haben möchte. Im besonderes dieses Grün das in beiden vorhanden ist versuche ich zu integrieren.
Habe selbst ein Etikett designet das aber sehr unprofessionell wirkt aber dieses Grüne das ich gerne als merkmal unterbringen würde.
Siehe Anhang: neemöl

```html
<!DOCTYPE html>
<html lang="de">
<head>
<meta charset="utf-8">
<title>Lavanda Vera – Etikett 155 × 32 mm</title>
<link href="https://fonts.googleapis.com/css2?family=Montserrat:wght@400;600&family=Dancing+Script:wght@700&display=swap" rel="stylesheet">
<style>
  :root {
    --ink-blue: #2e3a8f;
    --name-violet: #3b3a96;
    --leaf-deep: #5e9a10;
    --leaf-mid: #9cc920;
    --leaf-light: #dff08a;
    --volume-red: #850000;
    --trim-pink: #e8318a;
    --date-frame: #a4b877;
    --paper: #ffffff;
  }
  * { margin: 0; padding: 0; box-sizing: border-box; }
  html, body { width: 1200px; height: 462px; overflow: hidden; background: var(--paper); }
  body { font-family: "Montserrat", Arial, sans-serif; color: var(--ink-blue); }

  /* 155 × 32 mm → 1140 × 236 px */
  .label {
    position: absolute; left: 30px; top: 113px;
    width: 1140px; height: 236px; overflow: hidden;
  }

  .leaf-art {
    position: absolute; left: 0; top: 0; width: 960px; height: 236px;
    background:
      radial-gradient(ellipse 40% 75% at 8% 45%, var(--leaf-deep) 0%, rgba(94,154,16,0) 70%),
      linear-gradient(100deg, var(--leaf-mid) 0%, var(--leaf-light) 30%, #c6e05a 42%, rgba(240,248,220,0.6) 62%, rgba(255,255,255,0) 88%),
      linear-gradient(180deg, rgba(255,255,255,0) 70%, rgba(156,201,32,0.55) 100%);
  }

  .trim-line {
    position: absolute; left: 10px; top: 9px; width: 1120px; height: 218px;
    border: 1.5px solid var(--trim-pink);
  }

  .usage {
    position: absolute; left: 24px; top: 18px; width: 370px;
    font-size: 9.5px; line-height: 11.5px;
  }
  .usage p + p { margin-top: 3px; }
  .usage .lang-it { margin-top: 7px; }
  .usage strong { font-weight: 600; }

  .company {
    position: absolute; left: 26px; top: 150px; width: 380px;
    display: grid; grid-template-columns: 170px 210px;
    color: var(--paper); font-style: normal;
    font-size: 9px; line-height: 11px;
  }
  .company strong { font-weight: 600; }

  .flower-mark {
    position: absolute; left: 563px; top: 18px; width: 30px; height: 28px;
    background: linear-gradient(160deg, #b9a3e8 0%, #8b6fd0 45%, #c5e070 75%, #f1e85c 100%);
    border: 1px solid #fff;
  }

  .product-name {
    position: absolute; left: 0; width: 1156px; top: 52px; text-align: center;
    font-family: "Dancing Script", cursive; font-weight: 700;
    font-size: 58px; line-height: 1; color: var(--name-violet);
  }
  .product-kind {
    position: absolute; left: 0; width: 1156px; top: 118px; text-align: center;
    font-size: 15px; letter-spacing: 7px; color: #333a6e;
  }

  .volume-bar {
    position: absolute; left: 438px; top: 172px; width: 280px; height: 26px;
    background: var(--volume-red); color: var(--paper);
    font-size: 15px; line-height: 26px; text-align: center;
  }

  .info { position: absolute; left: 788px; top: 18px; width: 330px; }
  .warnings { font-size: 9.5px; line-height: 11.5px; }
  .warnings + .warnings { margin-top: 5px; }
  .bottling { margin-top: 8px; font-size: 10.5px; line-height: 12.5px; }
  .batch { margin-top: 4px; font-size: 8.5px; font-weight: 600; }
  .best-before { margin-top: 4px; font-size: 8px; }
  .date-field {
    margin-top: 2px; width: 190px; height: 34px;
    border: 1.5px solid var(--date-frame); background: var(--paper);
  }
</style>
</head>
<body>
<main class="label">
  <div class="leaf-art" role="img" aria-label="Geschwungene grüne und gelbe Blattbänder als Hintergrund"></div>
  <div class="trim-line"></div>

  <section class="usage">
    <p lang="de">100% natürliches etherisches Öl. Aroma-Kosmetikum zur Körperpflege.</p>
    <p lang="de"><strong>Anwendung:</strong> Als Haut- u. Massageöl max 15 Tr. Mit 50 ml z.B. Mandelöl mischen. Als Badezusatz 8-15 Tr. Auf 4 Eßl. Sahne oder Milch ins Badewasser geben.</p>
    <p class="lang-it" lang="it">100% olio essenziale naturale. Cosmetico aromatico per la cura del corpo.</p>
    <p lang="it"><strong>Uso:</strong> Come olio per pelle e massaggio max 15 gocce con 50 ml p.es. olio di mandorle. Nel bagno 8-15 gocce in 4 cucchiai di panna o latte.</p>
  </section>

  <address class="company">
    <span>
      <strong>Firmenname / Ditta:</strong><br>
      Bio des Hollmer Tobias<br>
      Talweg 14<br>
      I-39020 Valdoro<br>
      IVA: IT04518360291<br>
      CF.: HLLTBS88M12L219K
    </span>
    <span>
      <br>
      Tel: +39 0471/582716<br>
      Handy: 3408819263<br>
      https://www.natur-sefo.com/<br>
      info@natur-sefo.com
    </span>
  </address>

  <div class="flower-mark" role="img" aria-label="Kleines Bild einer violetten Blüte"></div>
  <h1 class="product-name">Lavanda</h1>
  <div class="product-kind">Vera</div>
  <div class="volume-bar">30 ml</div>

  <section class="info">
    <p class="warnings" lang="de">Nur in der angegeben Verdünnung anwenden! Nicht in die Augen oder auf die Schleimhäute bringen! Außer Reichweite von Kindern lagern.</p>
    <p class="warnings" lang="it">Usare solo nella diluizione indicata! Evitare il contatto con occhi e mucose! Tenere fuori dalla portata dei bambini.</p>
    <p class="bottling">Abgefüllt in Italien / Confezionato in Italia</p>
    <p class="batch">LottoNummer/CH nummer: 123456</p>
    <p class="best-before">Mindestens haltbar bis / Da consumarsi entro:</p>
    <div class="date-field"></div>
  </section>
</main>
</body>
</html>
```